Help me make landing pages for my web application that are mobile friendly

I need to make 2 mobile friendly landing pages for an application. The 2 pages will be related. First I need a home page and then I need a working page. I do not want to change the color scheme or logos. Just layout and design.

```html
<!DOCTYPE html>
<html lang="en">
<head>
<meta charset="utf-8">
<title>ShiftCover — Mobile Screens</title>
<link rel="stylesheet" href="https://fonts.googleapis.com/css2?family=Inter:wght@400;500;600&display=swap">
<style>
:root{
  --purple:#6b51a5;
  --teal:#29acd0;
  --teal-soft:#e4f5fa;
  --red:#e0444a;
  --red-soft:#fdeaea;
  --purple-soft:#eeebf6;
  --canvas-light:#f1f0f5;
  --white:#ffffff;
  --ink:#1d1d22;
  --ink-soft:#4f4f57;
  --muted:#a9a9b0;
  --line:#e3e3e9;
  --field:#fafafa;
  --avatar-a:#5b6570;
  --avatar-b:#b9a99a;
  --avatar-c:#6e4a3d;
}
*{box-sizing:border-box;margin:0;padding:0}
html,body{width:873px;height:1200px;overflow:hidden}
body{font-family:"Inter",sans-serif;color:var(--ink);background:var(--canvas-light)}
.stage{position:relative;width:1650px;height:2268px;transform:scale(0.52909);transform-origin:0 0}
.band{position:absolute;left:0;width:1650px}
.band--light{top:0;height:1134px;background:var(--canvas-light)}
.band--dark{top:1134px;height:1134px;background:var(--purple)}
.phone{position:absolute;width:423px;height:917px;border-radius:28px;background:var(--purple)}
.band--dark .phone{background:var(--canvas-light)}
.phone--home{left:108px}.phone--detail{left:613px}.phone--form{left:1118px}
.band .phone{top:108px}
.menu{position:absolute;left:27px;top:21px;width:19px;height:16px}
.menu span{display:block;height:2px;margin-bottom:5px;background:var(--white);border-radius:1px}
.band--dark .menu span{background:var(--purple)}
.brand{position:absolute;left:0;right:0;top:12px;display:flex;justify-content:center;align-items:center;gap:8px;height:34px;color:var(--white);font-size:22px;font-weight:500;letter-spacing:-.2px}
.brand__dot{width:20px;height:20px;border-radius:50%;background:currentColor}
.band--dark .brand{color:var(--purple)}
.panel{position:absolute;left:28px;top:64px;width:368px;height:826px;background:var(--white);border-radius:8px;overflow:hidden}
.band--dark .panel{border:1px solid var(--line)}
.panel__title{text-align:center;font-size:15px;font-weight:600;line-height:24px;padding-top:14px}
/* Home */
.tabs{display:flex;height:36px;margin:0 18px;font-size:13px}
.tab{flex:0 0 152px;text-align:center;line-height:40px;color:var(--ink)}
.tab--active{border-bottom:2px solid var(--purple)}
.tab + .tab{flex:1;margin-left:0}
.cards{padding:19px 18px 0}
.card{height:166px;border:1px solid var(--line);border-radius:8px;padding:17px 17px 0;margin-bottom:15px}
.card:last-child{margin-bottom:0}
.card__head{display:flex;align-items:center;gap:12px;height:53px;padding-bottom:13px;border-bottom:1px solid var(--line)}
.avatar{width:38px;height:38px;border-radius:50%;flex:none}
.avatar--a{background:var(--avatar-a)}.avatar--b{background:var(--avatar-b)}.avatar--c{background:var(--avatar-c)}
.person{flex:1}
.person__name{font-size:14.5px;font-weight:500;line-height:18px}
.person__role{font-size:13px;color:var(--ink-soft);line-height:17px}
.badge{font-size:11.5px;font-weight:500;padding:4px 13px;border-radius:2px;margin-top:-3px}
.badge--active{color:var(--teal);background:var(--teal-soft)}
.badge--canceled{color:var(--red);background:var(--red-soft)}
.badge--complete{color:var(--purple);background:var(--purple-soft)}
.card__facts{padding-top:9px;font-size:13.5px;color:var(--ink-soft)}
.fact{line-height:24.5px}
.fact b{color:var(--ink);font-weight:500;margin-right:4px}
.pager{display:flex;justify-content:center;align-items:center;gap:10px;margin-top:22px;font-size:11.5px;color:var(--ink-soft)}
.pager__item{width:26px;height:26px;line-height:26px;text-align:center}
.pager__item--current{background:var(--teal-soft);color:var(--teal);border-radius:2px}
.pager svg{width:26px;height:26px}
/* Detail */
.detail{padding:9px 18px 0}
.detail__row{font-size:15px;line-height:29px;color:var(--ink-soft)}
.detail__row b{color:var(--ink);font-weight:500;margin-right:4px}
.detail__label{font-size:15px;font-weight:500;line-height:29px;margin-top:6px}
.detail__text{font-size:14.5px;line-height:20px;color:var(--ink-soft);width:336px}
.actions{display:flex;gap:14px;margin-top:36px}
.btn{width:160px;height:44px;border-radius:3px;color:var(--white);font-size:15px;font-weight:500;display:flex;align-items:center;justify-content:center}
.btn--accept{background:var(--teal)}
.btn--decline{background:var(--purple)}
/* Form */
.form{padding:11px 18px 0}
.field{margin-bottom:10px}
.field__label{font-size:13px;font-weight:500;line-height:20px;margin-bottom:8px}
.input{height:42px;border:1px solid var(--line);background:var(--field);border-radius:2px;padding:0 9px;font-size:14.5px;color:var(--muted);line-height:40px}
.input--area{height:81px}
.input--wide{width:351px}
.split{display:flex;gap:13px}
.split .field{flex:0 0 160px}
</style>
</head>
<body>
<div class="stage">

  <section class="band band--light">
    <div class="phone phone--home">
      <div class="menu"><span></span><span></span><span></span></div>
      <div class="brand"><span class="brand__dot"></span>ShiftCover</div>
      <div class="panel">
        <nav class="tabs"><div class="tab tab--active">My Assignments</div><div class="tab">Available Openings</div></nav>
        <div class="cards">
          <article class="card"><div class="card__head"><div class="avatar avatar--a" role="img" aria-label="Profile photo of Marcus Hale"></div><div class="person"><div class="person__name">Marcus Hale</div><div class="person__role">Teacher</div></div><span class="badge badge--active">Active</span></div><div class="card__facts"><div class="fact"><b>Location:</b> Maple Grove Elementary School</div><div class="fact"><b>Date:</b> September 17, 2025</div><div class="fact"><b>Time Slot:</b> 8:00am - 2:00pm</div></div></article>
          <article class="card"><div class="card__head"><div class="avatar avatar--b" role="img" aria-label="Profile photo of Nora Bennett"></div><div class="person"><div class="person__name">Nora Bennett</div><div class="person__role">Teacher</div></div><span class="badge badge--canceled">Canceled</span></div><div class="card__facts"><div class="fact"><b>Location:</b> Cedar Ridge Middle School</div><div class="fact"><b>Date:</b> September 21, 2025</div><div class="fact"><b>Time Slot:</b> 8:00am - 12:00pm</div></div></article>
          <article class="card"><div class="card__head"><div class="avatar avatar--a" role="img" aria-label="Profile photo of Owen Carter"></div><div class="person"><div class="person__name">Owen Carter</div><div class="person__role">Teacher</div></div><span class="badge badge--complete">Complete</span></div><div class="card__facts"><div class="fact"><b>Location:</b> Lakeview High School</div><div class="fact"><b>Date:</b> September 15, 2025</div><div class="fact"><b>Time Slot:</b> 12:00am - 2:00pm</div></div></article>
          <article class="card"><div class="card__head"><div class="avatar avatar--c" role="img" aria-label="Profile photo of Claire Morgan"></div><div class="person"><div class="person__name">Claire Morgan</div><div class="person__role">Administrator</div></div><span class="badge badge--complete">Complete</span></div><div class="card__facts"><div class="fact"><b>Location:</b> Pine Hollow High School</div><div class="fact"><b>Date:</b> September 13, 2025</div><div class="fact"><b>Time Slot:</b> 6:00am -4:00pm</div></div></article>
        </div>
        <div class="pager"><svg viewBox="0 0 26 26"><path d="M15 8l-5 5 5 5" fill="none" stroke="#4f4f57" stroke-width="1.5"/></svg><span class="pager__item pager__item--current">1</span><span class="pager__item">2</span><span class="pager__item">3</span><span class="pager__item">4</span><svg viewBox="0 0 26 26"><path d="M11 8l5 5-5 5" fill="none" stroke="#4f4f57" stroke-width="1.5"/></svg></div>
      </div>
    </div>

    <div class="phone phone--detail">
      <div class="menu"><span></span><span></span><span></span></div>
      <div class="brand"><span class="brand__dot"></span>ShiftCover</div>
      <div class="panel">
        <h2 class="panel__title">Assignment Details</h2>
        <div class="detail">
          <p class="detail__row"><b>Title:</b> 8th Grade Math Substitute</p>
          <p class="detail__row"><b>Location:</b> Maple Grove Elementary School</p>
          <p class="detail__row"><b>Date:</b> September 17, 2025</p>
          <p class="detail__row"><b>Department:</b> Mathematics</p>
          <p class="detail__row"><b>Department:</b> Mathematics</p>
          <p class="detail__row"><b>Regular Staff:</b> Marcus Hale</p>
          <p class="detail__row"><b>Type:</b> Vacancy</p>
          <p class="detail__label">Description:</p>
          <p class="detail__text">The ideal candidate will be able to follow the provided lesson plan, maintain a positive and engaging classroom environment, and assist students with their assigned work. The main topics for the day will be algebraic equations and problem-solving strategies. Strong classroom management skills and a passion for education are a must.</p>
          <div class="actions"><span class="btn btn--accept">Accept</span><span class="btn btn--decline">Decline</span></div>
        </div>
      </div>
    </div>

    <div class="phone phone--form">
      <div class="menu"><span></span><span></span><span></span></div>
      <div class="brand"><span class="brand__dot"></span>ShiftCover</div>
      <div class="panel">
        <h2 class="panel__title">New Assignment</h2>
        <div class="form">
          <div class="field"><div class="field__label">Title</div><div class="input">Placeholder</div></div>
          <div class="field"><div class="field__label">Location</div><div class="input">Placeholder</div></div>
          <div class="field"><div class="field__label">Date</div><div class="input">Placeholder</div></div>
          <div class="split"><div class="field"><div class="field__label">Start Time</div><div class="input">Placeholder</div></div><div class="field"><div class="field__label">End Time</div><div class="input">Placeholder</div></div></div>
          <div class="field"><div class="field__label">Description</div><div class="input input--area">Placeholder</div></div>
          <div class="field"><div class="field__label">Department</div><div class="input">Placeholder</div></div>
          <div class="field"><div class="field__label">Regular Staff</div><div class="input">Placeholder</div></div>
          <div class="field"><div class="field__label">Type</div><div class="input">Placeholder</div></div>
          <div class="field"><div class="field__label">Additional Details</div><div class="input input--area input--wide">Placeholder</div></div>
        </div>
      </div>
    </div>
  </section>

  <section class="band band--dark">
    <div class="phone phone--home">
      <div class="menu"><span></span><span></span><span></span></div>
      <div class="brand"><span class="brand__dot"></span>ShiftCover</div>
      <div class="panel">
        <nav class="tabs"><div class="tab tab--active">My Assignments</div><div class="tab">Available Openings</div></nav>
        <div class="cards">
          <article class="card"><div class="card__head"><div class="avatar avatar--a" role="img" aria-label="Profile photo of Marcus Hale"></div><div class="person"><div class="person__name">Marcus Hale</div><div class="person__role">Teacher</div></div><span class="badge badge--active">Active</span></div><div class="card__facts"><div class="fact"><b>Location:</b> Maple Grove Elementary School</div><div class="fact"><b>Date:</b> September 17, 2025</div><div class="fact"><b>Time Slot:</b> 8:00am - 2:00pm</div></div></article>
          <article class="card"><div class="card__head"><div class="avatar avatar--b" role="img" aria-label="Profile photo of Nora Bennett"></div><div class="person"><div class="person__name">Nora Bennett</div><div class="person__role">Teacher</div></div><span class="badge badge--canceled">Canceled</span></div><div class="card__facts"><div class="fact"><b>Location:</b> Cedar Ridge Middle School</div><div class="fact"><b>Date:</b> September 21, 2025</div><div class="fact"><b>Time Slot:</b> 8:00am - 12:00pm</div></div></article>
          <article class="card"><div class="card__head"><div class="avatar avatar--a" role="img" aria-label="Profile photo of Owen Carter"></div><div class="person"><div class="person__name">Owen Carter</div><div class="person__role">Teacher</div></div><span class="badge badge--complete">Complete</span></div><div class="card__facts"><div class="fact"><b>Location:</b> Lakeview High School</div><div class="fact"><b>Date:</b> September 15, 2025</div><div class="fact"><b>Time Slot:</b> 12:00am - 2:00pm</div></div></article>
          <article class="card"><div class="card__head"><div class="avatar avatar--c" role="img" aria-label="Profile photo of Claire Morgan"></div><div class="person"><div class="person__name">Claire Morgan</div><div class="person__role">Administrator</div></div><span class="badge badge--complete">Complete</span></div><div class="card__facts"><div class="fact"><b>Location:</b> Pine Hollow High School</div><div class="fact"><b>Date:</b> September 13, 2025</div><div class="fact"><b>Time Slot:</b> 6:00am -4:00pm</div></div></article>
        </div>
        <div class="pager"><svg viewBox="0 0 26 26"><path d="M15 8l-5 5 5 5" fill="none" stroke="#4f4f57" stroke-width="1.5"/></svg><span class="pager__item pager__item--current">1</span><span class="pager__item">2</span><span class="pager__item">3</span><span class="pager__item">4</span><svg viewBox="0 0 26 26"><path d="M11 8l5 5-5 5" fill="none" stroke="#4f4f57" stroke-width="1.5"/></svg></div>
      </div>
    </div>

    <div class="phone phone--detail">
      <div class="menu"><span></span><span></span><span></span></div>
      <div class="brand"><span class="brand__dot"></span>ShiftCover</div>
      <div class="panel">
        <h2 class="panel__title">Assignment Details</h2>
        <div class="detail">
          <p class="detail__row"><b>Title:</b> 8th Grade Math Substitute</p>
          <p class="detail__row"><b>Location:</b> Maple Grove Elementary School</p>
          <p class="detail__row"><b>Date:</b> September 17, 2025</p>
          <p class="detail__row"><b>Department:</b> Mathematics</p>
          <p class="detail__row"><b>Department:</b> Mathematics</p>
          <p class="detail__row"><b>Regular Staff:</b> Marcus Hale</p>
          <p class="detail__row"><b>Type:</b> Vacancy</p>
          <p class="detail__label">Description:</p>
          <p class="detail__text">The ideal candidate will be able to follow the provided lesson plan, maintain a positive and engaging classroom environment, and assist students with their assigned work. The main topics for the day will be algebraic equations and problem-solving strategies. Strong classroom management skills and a passion for education are a must.</p>
          <div class="actions"><span class="btn btn--accept">Accept</span><span class="btn btn--decline">Decline</span></div>
        </div>
      </div>
    </div>

    <div class="phone phone--form">
      <div class="menu"><span></span><span></span><span></span></div>
      <div class="brand"><span class="brand__dot"></span>ShiftCover</div>
      <div class="panel">
        <h2 class="panel__title">New Assignment</h2>
        <div class="form">
          <div class="field"><div class="field__label">Title</div><div class="input">Placeholder</div></div>
          <div class="field"><div class="field__label">Location</div><div class="input">Placeholder</div></div>
          <div class="field"><div class="field__label">Date</div><div class="input">Placeholder</div></div>
          <div class="split"><div class="field"><div class="field__label">Start Time</div><div class="input">Placeholder</div></div><div class="field"><div class="field__label">End Time</div><div class="input">Placeholder</div></div></div>
          <div class="field"><div class="field__label">Description</div><div class="input input--area">Placeholder</div></div>
          <div class="field"><div class="field__label">Department</div><div class="input">Placeholder</div></div>
          <div class="field"><div class="field__label">Regular Staff</div><div class="input">Placeholder</div></div>
          <div class="field"><div class="field__label">Type</div><div class="input">Placeholder</div></div>
          <div class="field"><div class="field__label">Additional Details</div><div class="input input--area input--wide">Placeholder</div></div>
        </div>
      </div>
    </div>
  </section>

</div>
</body>
</html>
```